Kelbrook LLC web design project

Dallas, TX based water damage mitigation company needs a web site for its new business. The company does water extractions, mitigation, demo, restoration, and reconstruction. We need for the site to have a strong mobile version, and the owners/managers need to be able to edit the site despite having no web design experience. The site needs to look and function, especially the mobile version, similar to bramfieldorchardworks.com if possible.

```html
<!DOCTYPE html>
<html lang="en">
<head>
<meta charset="utf-8">
<title>Kelbrook LLC</title>
<link href="https://fonts.googleapis.com/css2?family=Lato:ital,wght@0,400;0,700;0,900;1,400&family=Ubuntu:wght@500;700&family=Russo+One&display=swap" rel="stylesheet">
<style>
:root{
  --blue:#1565c0;
  --blue-dark:#0f52a3;
  --navy:#2b3344;
  --ink:#222;
  --muted:#444;
  --light:#f2f4f7;
  --white:#fff;
}
*{margin:0;padding:0;box-sizing:border-box}
html,body{width:1200px;height:3589px;overflow:hidden}
body{position:relative;font-family:"Lato",sans-serif;color:var(--ink);background:var(--light)}
.abs{position:absolute}
.topbar{left:0;top:0;width:1200px;height:44px;background:var(--navy);color:#fff;font:700 11px/44px "Lato",sans-serif}
.topbar span{position:absolute;top:0;display:flex;align-items:center;gap:7px;height:44px}
.nav{left:0;top:44px;width:1200px;height:55px;background:#fff}
.nav a{position:absolute;top:0;font:700 12px/55px "Lato",sans-serif;color:#222;text-decoration:none;letter-spacing:.3px}
.nav .sep{position:absolute;top:0;line-height:55px;font-size:12px;color:#333}
.nav .contact{left:920px;width:167px;height:55px;background:var(--blue);color:#fff;text-align:center;font:700 15px/55px "Ubuntu",sans-serif}
.brandbox{left:502px;top:0;width:195px;height:150px;z-index:3}
.brandname{position:absolute;left:0;width:195px;top:80px;text-align:center;font:700 22px "Ubuntu",sans-serif;color:var(--blue)}
.hero{left:0;top:99px;width:1200px;height:615px;background:linear-gradient(160deg,#6b7a88 0%,#4c5660 35%,#3f4650 60%,#5d5346 100%)}
.hero-glow{left:0;top:99px;width:1200px;height:615px;background:radial-gradient(ellipse at 75% 20%,rgba(230,190,140,.35),transparent 55%)}
.hero-sub{left:599px;top:254px;font:500 39px "Ubuntu",sans-serif;color:#fff}
.hero-title{left:599px;top:294px;font:700 62px "Ubuntu",sans-serif;color:#fff;letter-spacing:.5px;white-space:nowrap}
.hero-text{left:599px;top:376px;width:460px;font:400 14.5px/28px "Lato",sans-serif;color:#fff}
.btn{display:block;background:var(--blue);color:#fff;text-align:center;font:700 15px "Ubuntu",sans-serif;border-radius:4px;text-decoration:none}
.dots{left:569px;top:629px;display:flex;gap:5px}
.dots i{width:9px;height:9px;border-radius:50%;background:#fff}
.dots i:first-child{background:var(--blue)}
.band{left:0;top:714px;width:1200px;height:8px;background:var(--blue)}
.about{left:0;top:722px;width:1200px;height:630px;background:#fff}
.label{font:700 15px "Lato",sans-serif;color:#222}
.title{font:700 31px "Ubuntu",sans-serif;color:var(--blue)}
.rule{height:2px;background:var(--blue)}
.about-text{left:93px;top:970px;width:500px;font:400 13.5px/26.5px "Lato",sans-serif;color:#333;text-align:justify}
.about-photo{left:627px;top:764px;width:573px;height:588px;background:linear-gradient(135deg,#5f86b3 0%,#9aa69c 55%,#c9c55a 100%)}
.services{left:0;top:1352px;width:1200px;height:772px;background:linear-gradient(180deg,#1a64b8,#1565c0 60%,#1a6ac4)}
.center{left:0;width:1200px;text-align:center}
.card{width:258px;height:272px;background:#fff;box-shadow:0 3px 10px rgba(0,0,0,.12);text-align:center}
.card svg{position:absolute;left:70px;top:0}
.card h3{position:absolute;left:0;width:100%;top:104px;font:400 16px "Russo One",sans-serif;color:var(--blue);letter-spacing:.5px}
.card p{position:absolute;left:22px;width:214px;top:134px;font:400 13.5px/28px "Lato",sans-serif;color:#333}
.avatar{left:529px;top:2392px;width:72px;height:72px;border-radius:50%;background:linear-gradient(135deg,#b9bec4,#6d7680)}
.who{left:619px;top:2405px}
.who b{display:block;font:700 15px "Ubuntu",sans-serif;color:var(--blue)}
.who span{display:block;font:400 15px "Lato",sans-serif;color:#333;margin-top:6px}
.quote{left:250px;top:2476px;width:795px;text-align:center;font:italic 400 13.5px/35px "Lato",sans-serif;color:#333}
.qm{font:900 44px/1 "Lato",sans-serif;color:var(--blue)}
.news-photo{height:206px}
.caption{width:257px;height:94px;background:#fff;box-shadow:0 3px 8px rgba(0,0,0,.18);text-align:center}
.caption b{display:block;margin-top:14px;font:700 14px "Lato",sans-serif;color:#222}
.caption span{display:block;margin-top:6px;font:400 11.5px/24px "Lato",sans-serif;color:#333}
.circle{border-radius:50%;background:var(--blue)}
.footer{left:0;top:3240px;width:1200px;height:349px;background:var(--navy);color:#fff}
.footer-brand{left:120px;top:158px;width:234px;text-align:center;font:700 26px "Lato",sans-serif;color:#fff;white-space:nowrap}
.fhead{font:700 15px "Lato",sans-serif;color:#fff;letter-spacing:.4px}
.flist{list-style:none;font:400 13.5px/28px "Lato",sans-serif;color:#eee}
.flist li::before{content:"»";margin-right:9px}
.fcontact{font:400 13.5px/21px "Lato",sans-serif;color:#eee}
</style>
</head>
<body>

<div class="abs topbar">
  <span style="left:144px">CALL NOW FOR A FREE QUOTE!</span>
  <span style="left:734px"><svg width="11" height="11" viewBox="0 0 24 24"><path fill="#fff" d="M6.6 10.8a15 15 0 0 0 6.6 6.6l2.2-2.2c.3-.3.7-.4 1-.2 1.1.4 2.3.6 3.6.6.6 0 1 .4 1 1V20c0 .6-.4 1-1 1A17 17 0 0 1 3 4c0-.6.4-1 1-1h3.5c.6 0 1 .4 1 1 0 1.3.2 2.5.6 3.6.1.3 0 .7-.2 1z"/></svg>+1 555 014 2290</span>
  <span style="left:877px"><svg width="12" height="10" viewBox="0 0 24 18"><rect width="24" height="18" rx="2" fill="#fff"/><path d="M1 2l11 8 11-8" stroke="#2b3344" stroke-width="2" fill="none"/></svg>hello@kelbrookmail.com</span>
</div>

<div class="abs nav">
  <a style="left:173px">HOME</a><span class="sep" style="left:234px">|</span>
  <a style="left:262px">ABOUT US</a><span class="sep" style="left:348px">|</span>
  <a style="left:376px">SERVICES</a>
  <a style="left:737px">NEWS</a><span class="sep" style="left:797px">|</span>
  <a style="left:825px">PROJECT</a>
  <a class="contact">CONTACT US</a>
</div>

<div class="abs brandbox">
  <svg width="195" height="150" viewBox="0 0 195 150"><polygon points="0,0 195,0 195,118 97.5,148 0,118" fill="#fff"/></svg>
  <div class="brandname">KELBROOK LLC</div>
</div>

<div class="abs hero" role="img" aria-label="Aerial photo of a city skyline at dusk with a large faint mascot graphic on the left"></div>
<div class="abs hero-glow"></div>
<div class="abs hero-sub">WELCOME TO</div>
<div class="abs hero-title">KELBROOK LLC</div>
<p class="abs hero-text">Lorem ipsum dolor sit amet, consectetur adipiscing elit, sed do eiusmod tempor incididunt ut labore et dolore magna aliqua. Ut enim ad minim veniam, quis nostrud exercitation.</p>
<a class="abs btn" style="left:599px;top:478px;width:188px;height:48px;line-height:48px">GET STARTED</a>
<div class="abs dots"><i></i><i></i><i></i><i></i><i></i></div>
<div class="abs band"></div>

<div class="abs about"></div>
<div class="abs label" style="left:93px;top:872px">ABOUT US</div>
<div class="abs title" style="left:91px;top:896px">KELBROOK LLC</div>
<div class="abs rule" style="left:93px;top:946px;width:42px"></div>
<p class="abs about-text">Lorem ipsum dolor sit amet, consectetur adipiscing elit, sed do eiusmod tempor incididunt ut labore et dolore magna aliqua. Quis ipsum suspendisse ultrices gravida. Risus commodo viverra maecenas accumsan lacus vel facilisis. Sed ut perspiciatis unde omnis iste natus error sit voluptatem accusantium doloremque laudantium, totam rem aperiam, eaque ipsa quae ab illo inventore veritatis et quasi architecto beatae vitae dicta sunt explicabo. Nemo enim ipsam voluptatem quia voluptas sit aspernatur aut odit aut fugit, sed quia consequuntur magni dolores eos qui ratione voluptatem sequi nesciunt. Neque porro quisquam est, qui dolorem ipsum quia dolor sit amet consectetur.</p>
<a class="abs btn" style="left:95px;top:1225px;width:188px;height:49px;line-height:49px">LEARN MORE</a>
<div class="abs about-photo" role="img" aria-label="Photo of a bearded worker in a hard hat and safety vest holding a laptop, over a city map backdrop"></div>

<div class="abs services" role="img" aria-label="Faint city skyline photo under a blue overlay"></div>
<div class="abs center" style="top:1428px;font:700 15px 'Lato',sans-serif;color:#fff">OUR SERVICES</div>
<div class="abs center" style="top:1452px;font:700 31px 'Ubuntu',sans-serif;color:#fff">WHAT WE DO</div>
<div class="abs rule" style="left:558px;top:1502px;width:84px;background:#fff"></div>

<div class="abs card" style="left:158px;top:1570px"><svg width="118" height="90" viewBox="0 0 118 90"><polygon points="28,0 90,0 118,45 90,90 28,90 0,45" fill="#1565c0"/><g stroke="#fff" stroke-width="2.5" fill="none"><rect x="40" y="30" width="14" height="38"/><rect x="54" y="18" width="14" height="50"/><rect x="68" y="36" width="12" height="32"/></g></svg><h3>LOREM IPSUM DOLOR</h3><p>Lorem ipsum dolor sit amet, consectetur adipiscing elit, sed do eiusmod tempor incididunt ut labore et dolore magna aliqua.</p></div>
<div class="abs card" style="left:471px;top:1570px"><svg width="118" height="90" viewBox="0 0 118 90"><polygon points="28,0 90,0 118,45 90,90 28,90 0,45" fill="#1565c0"/><g stroke="#fff" stroke-width="2.5" fill="none"><path d="M38 62h42M44 62v-14a15 15 0 0 1 30 0v14"/><circle cx="76" cy="28" r="6"/><path d="M42 22l10 14"/></g></svg><h3>LOREM IPSUM DOLOR</h3><p>Lorem ipsum dolor sit amet, consectetur adipiscing elit, sed do eiusmod tempor incididunt ut labore et dolore magna aliqua.</p></div>
<div class="abs card" style="left:785px;top:1570px"><svg width="118" height="90" viewBox="0 0 118 90"><polygon points="28,0 90,0 118,45 90,90 28,90 0,45" fill="#1565c0"/><g stroke="#fff" stroke-width="2.5" fill="none"><path d="M60 68V20M44 22h36M76 22v12"/><rect x="40" y="44" width="12" height="24"/><path d="M54 68h16"/></g></svg><h3>LOREM IPSUM DOLOR</h3><p>Lorem ipsum dolor sit amet, consectetur adipiscing elit, sed do eiusmod tempor incididunt ut labore et dolore magna aliqua.</p></div>
<div class="abs card" style="left:158px;top:1905px"><svg width="118" height="90" viewBox="0 0 118 90"><polygon points="28,0 90,0 118,45 90,90 28,90 0,45" fill="#1565c0"/><g stroke="#fff" stroke-width="2.5" fill="none"><rect x="52" y="44" width="26" height="14"/><circle cx="56" cy="64" r="4"/><circle cx="74" cy="64" r="4"/><path d="M52 44l-8-18-6 14"/></g></svg><h3>LOREM IPSUM DOLOR</h3><p>Lorem ipsum dolor sit amet, consectetur adipiscing elit, sed do eiusmod tempor incididunt ut labore et dolore magna aliqua.</p></div>
<div class="abs card" style="left:471px;top:1905px"><svg width="118" height="90" viewBox="0 0 118 90"><polygon points="28,0 90,0 118,45 90,90 28,90 0,45" fill="#1565c0"/><g stroke="#fff" stroke-width="2.5" fill="none"><rect x="40" y="22" width="34" height="44"/><path d="M46 34h22M46 44h22M46 54h14M74 30l8 4v36l-30-2"/></g></svg><h3>LOREM IPSUM DOLOR</h3><p>Lorem ipsum dolor sit amet, consectetur adipiscing elit, sed do eiusmod tempor incididunt ut labore et dolore magna aliqua.</p></div>
<div class="abs card" style="left:785px;top:1905px"><svg width="118" height="90" viewBox="0 0 118 90"><polygon points="28,0 90,0 118,45 90,90 28,90 0,45" fill="#1565c0"/><g stroke="#fff" stroke-width="2.5" fill="none"><rect x="40" y="48" width="36" height="18"/><path d="M44 48V36h14v12M62 48l8-22 8 4"/></g></svg><h3>LOREM IPSUM DOLOR</h3><p>Lorem ipsum dolor sit amet, consectetur adipiscing elit, sed do eiusmod tempor incididunt ut labore et dolore magna aliqua.</p></div>

<div class="abs center" style="top:2279px;font:700 15px 'Lato',sans-serif;color:#222">REVIEW</div>
<div class="abs center" style="top:2303px;font:700 31px 'Ubuntu',sans-serif;color:var(--blue)">OUR CLIENT TESTIMONIALS</div>
<div class="abs rule" style="left:558px;top:2352px;width:84px"></div>
<div class="abs avatar" role="img" aria-label="Client portrait photo"></div>
<div class="abs who"><b>DANA WHITFIELD</b><span>Lorem Ipsum</span></div>
<div class="abs quote"><span class="qm" style="position:absolute;left:-20px;top:-6px">"</span>Lorem ipsum dolor sit amet, consectetur adipiscing elit, sed do eiusmod tempor incididunt ut labore et dolore magna aliqua. Ut enim ad minim veniam, quis nostrud exercitation ullamco laboris nisi ut aliquip ex ea commodo consequat. Duis aute irure dolor in reprehenderit in voluptate velit esse cillum dolore eu fugiat nulla pariatur. Excepteur sint occaecat cupidatat non proident, sunt in culpa qui officia deserunt mollit anim id est laborum. <span class="qm" style="vertical-align:-14px">"</span></div>
<svg class="abs" style="left:157px;top:2512px" width="20" height="32" viewBox="0 0 20 32"><path d="M16 3L4 16l12 13" stroke="#222" stroke-width="4" fill="none"/></svg>
<svg class="abs" style="left:1093px;top:2512px" width="20" height="32" viewBox="0 0 20 32"><path d="M4 3l12 13L4 29" stroke="#222" stroke-width="4" fill="none"/></svg>

<svg class="abs" style="left:0;top:2662px" width="1200" height="570" viewBox="0 0 1200 570"><polygon points="0,91 600,0 1200,91 1200,570 0,570" fill="#fff"/></svg>
<div class="abs center" style="top:2782px;font:700 15px 'Lato',sans-serif;color:#222">NEWS</div>
<div class="abs center" style="top:2806px;font:700 31px 'Ubuntu',sans-serif;color:var(--blue)">OUR LATEST NEWS</div>
<div class="abs rule" style="left:558px;top:2855px;width:84px"></div>

<div class="abs news-photo" style="left:149px;top:2901px;width:291px;background:linear-gradient(135deg,#8a7456,#5b4a36 60%,#c9b792)" role="img" aria-label="Photo of a water-damaged room with exposed wall studs"></div>
<div class="abs news-photo" style="left:453px;top:2901px;width:291px;background:linear-gradient(135deg,#c9c4bd,#8d8379 55%,#dcd6cf)" role="img" aria-label="Photo of a plumber working under a bathroom sink"></div>
<div class="abs news-photo" style="left:756px;top:2901px;width:291px;background:linear-gradient(135deg,#a9a7a2,#4d6ea0 55%,#2b4f8a)" role="img" aria-label="Photo of a worker in a blue hard hat repairing pipes"></div>
<div class="abs caption" style="left:167px;top:3077px"><b>LOREM IPSUM DOLOR SIT</b><span>Lorem ipsum dolor sit amet, consect<br>etur adipiscing elit, sed do</span></div>
<div class="abs caption" style="left:471px;top:3077px"><b>LOREM IPSUM DOLOR SIT</b><span>Lorem ipsum dolor sit amet, consect<br>etur adipiscing elit, sed do</span></div>
<div class="abs caption" style="left:774px;top:3077px"><b>LOREM IPSUM DOLOR SIT</b><span>Lorem ipsum dolor sit amet, consect<br>etur adipiscing elit, sed do</span></div>
<svg class="abs" style="left:129px;top:2984px" width="40" height="40" viewBox="0 0 40 40"><circle cx="20" cy="20" r="20" fill="#1565c0"/><path d="M22 14l-6 6 6 6" stroke="#fff" stroke-width="2" fill="none"/></svg>
<svg class="abs" style="left:1030px;top:2984px" width="40" height="40" viewBox="0 0 40 40"><circle cx="20" cy="20" r="20" fill="#1565c0"/><path d="M18 14l6 6-6 6" stroke="#fff" stroke-width="2" fill="none"/></svg>

<div class="abs" style="left:0;top:3231px;width:1200px;height:9px;background:var(--blue)"></div>
<div class="abs footer">
  <div class="abs footer-brand">KELBROOK LLC</div>
  <div class="abs fhead" style="left:406px;top:78px">QUICK LINKS</div>
  <ul class="abs flist" style="left:406px;top:103px"><li>Home</li><li>Services</li><li>Project</li><li>News</li></ul>
  <div class="abs fhead" style="left:606px;top:78px">LEGAL</div>
  <ul class="abs flist" style="left:603px;top:103px"><li>Privacy Policy</li><li>Terms &amp; Conditions</li><li>Contact Us</li><li>About Us</li></ul>
  <div class="abs fhead" style="left:831px;top:78px">CONTACT US</div>
  <div class="abs fcontact" style="left:831px;top:107px;width:270px">
    <div style="display:flex;gap:12px"><svg width="9" height="13" viewBox="0 0 12 18" style="margin-top:3px;flex:none"><path d="M6 0a6 6 0 0 0-6 6c0 4.5 6 12 6 12s6-7.5 6-12a6 6 0 0 0-6-6zm0 8.5A2.5 2.5 0 1 1 6 3.5a2.5 2.5 0 0 1 0 5z" fill="#fff"/></svg><span>123 Sed ut perspiciatis unde omnis<br>iste natus error sit voluptatem</span></div>
    <div style="display:flex;gap:12px;margin-top:17px;align-items:center"><svg width="12" height="12" viewBox="0 0 24 24"><path fill="#fff" d="M6.6 10.8a15 15 0 0 0 6.6 6.6l2.2-2.2c.3-.3.7-.4 1-.2 1.1.4 2.3.6 3.6.6.6 0 1 .4 1 1V20c0 .6-.4 1-1 1A17 17 0 0 1 3 4c0-.6.4-1 1-1h3.5c.6 0 1 .4 1 1 0 1.3.2 2.5.6 3.6.1.3 0 .7-.2 1z"/></svg><span>555 014 7731</span></div>
    <div style="display:flex;gap:12px;margin-top:19px;align-items:center"><svg width="13" height="10" viewBox="0 0 24 18"><rect width="24" height="18" rx="2" fill="#fff"/><path d="M1 2l11 8 11-8" stroke="#2b3344" stroke-width="2" fill="none"/></svg><span>office@kelbrookmail.com</span></div>
  </div>
  <div class="abs" style="left:102px;top:255px;width:981px;height:1px;background:#8a919c"></div>
  <div class="abs circle" style="left:148px;top:266px;width:30px;height:30px"></div>
  <div class="abs circle" style="left:191px;top:266px;width:30px;height:30px"></div>
  <div class="abs circle" style="left:236px;top:266px;width:30px;height:30px"></div>
  <div class="abs circle" style="left:279px;top:266px;width:30px;height:30px"></div>
  <div class="abs" style="right:145px;top:274px;font:400 12px 'Lato',sans-serif;color:#fff;white-space:nowrap">© Copyright 2022 &nbsp;<b>KELBROOK LLC</b> &nbsp;| &nbsp;&nbsp;All Rights Reserved</div>
</div>

</body>
</html>
```